Walking Beside the Quiet River; A Study of Refuge, Purpose & Calling

I need a book cover, for the above book title. This is a journey of the heart to know the heart of God. I think on the text, Simple (see below graphic)
Black Lettering for Knowing.....Intimately
Gold lettering for God
Either gold or black for the subtitle; A Study of Refuge, Purpose, & Calling
I would like the below graphic idea only no photograph of a person,
and White background instead of black
Simple Font, like below graphic, but open to suggestions

Target Market(s)

not age specific, Every person has been given a heart to know God, we are taking the mystery out the process to understand God is Father, loving gracious, ever present, etc. If we know His heart, we realize He's not at a distance, He is there, an ever present help

Industry/Entity Type

Security

Requirements
Must have
• Title: Walking Beside the Quiet River; A Study of Refuge, Purpose, & Calling
• My name, Tom Pettigrew
Nice to have
• See Below Graphic

```html
<!DOCTYPE html>
<html lang="en">
<head>
<meta charset="utf-8">
<title>Walking Beside the Quiet River — Book Cover</title>
<link rel="stylesheet" href="https://fonts.googleapis.com/css2?family=Cinzel:wght@400;500&display=swap">
<style>
  :root {
    --page-bg: #f4f4f2;
    --cover-white: #ffffff;
    --cover-edge: #e6e6e3;
    --cover-line: #d6d6d2;
    --ink-black: #141414;
    --gold-light: #f2c73c;
    --gold-mid: #d99e18;
    --gold-deep: #a8690c;
    --glow-core: #fdf6d8;
    --glow-mid: #f3e2a6;
    --glow-edge: #e9d59a;
  }
  * { box-sizing: border-box; margin: 0; padding: 0; }
  html, body {
    width: 1200px;
    height: 1200px;
    overflow: hidden;
    background: var(--page-bg);
  }
  .stage {
    position: relative;
    width: 1200px;
    height: 1200px;
    display: flex;
    align-items: center;
    justify-content: center;
    gap: 111px;
  }
  .cover-front {
    position: relative;
    width: 544px;
    height: 760px;
    background: linear-gradient(90deg, var(--cover-edge) 0%, var(--cover-white) 10%, var(--cover-white) 100%);
    border: 1px solid var(--cover-line);
    overflow: hidden;
    font-family: "Cinzel", serif;
    color: var(--ink-black);
    text-align: center;
  }
  .cover-art {
    position: absolute;
    left: 0;
    top: 300px;
    width: 100%;
    height: 460px;
    background:
      radial-gradient(ellipse 220px 230px at 58% 50%, var(--glow-core) 0%, var(--glow-mid) 40%, rgba(233,213,154,0.45) 70%, rgba(255,255,255,0) 100%);
  }
  .cover-art::after {
    content: "";
    position: absolute;
    left: 0; right: 0; bottom: 0;
    height: 150px;
    background: linear-gradient(180deg, rgba(255,255,255,0) 0%, rgba(255,255,255,0.85) 60%, var(--cover-white) 100%);
  }
  .title-block {
    position: relative;
    padding-top: 52px;
  }
  .title {
    font-weight: 400;
  }
  .title-lead {
    display: block;
    font-size: 30px;
    letter-spacing: 0.08em;
    line-height: 1;
  }
  .title-feature {
    display: block;
    font-size: 122px;
    font-weight: 400;
    line-height: 1;
    margin-top: 20px;
    background: linear-gradient(180deg, var(--gold-light) 0%, var(--gold-mid) 55%, var(--gold-deep) 100%);
    -webkit-background-clip: text;
    background-clip: text;
    color: transparent;
  }
  .title-tail {
    display: block;
    font-size: 52px;
    letter-spacing: 0.08em;
    line-height: 1;
    margin-top: 14px;
  }
  .subtitle {
    font-size: 19px;
    letter-spacing: 0.06em;
    line-height: 1.55;
    margin-top: 18px;
  }
  .author {
    position: absolute;
    left: 0; right: 0;
    bottom: 52px;
    font-size: 40px;
    letter-spacing: 0.08em;
    line-height: 1;
  }
  .author .small-cap { font-size: 31px; }

  .cover-spine {
    position: relative;
    width: 96px;
    height: 760px;
    background: linear-gradient(90deg, #ececea 0%, #ffffff 22%, #f7f7f5 60%, #e4e4e1 100%);
    border: 1px solid var(--cover-line);
    display: flex;
    justify-content: center;
    padding: 30px 0;
    font-family: "Cinzel", serif;
    color: var(--ink-black);
  }
  .spine-text {
    writing-mode: vertical-rl;
    display: flex;
    align-items: center;
    white-space: nowrap;
    width: 100%;
    justify-content: space-between;
  }
  .spine-title {
    display: flex;
    align-items: center;
    gap: 10px;
    font-size: 17px;
    letter-spacing: 0.1em;
  }
  .spine-feature {
    font-size: 34px;
    letter-spacing: 0.02em;
    background: linear-gradient(90deg, var(--gold-light) 0%, var(--gold-mid) 55%, var(--gold-deep) 100%);
    -webkit-background-clip: text;
    background-clip: text;
    color: transparent;
  }
  .spine-author {
    font-size: 19px;
    letter-spacing: 0.1em;
  }
</style>
</head>
<body>
  <main class="stage">
    <section class="cover-front">
      <div class="cover-art" role="img" aria-label="Soft warm lantern light glowing in an open space"></div>
      <header class="title-block">
        <h1 class="title">
          <span class="title-lead">WALKING BESIDE THE</span>
          <span class="title-feature">QUIET</span>
          <span class="title-tail">RIVER</span>
        </h1>
        <p class="subtitle">A STUDY OF REFUGE,<br>PURPOSE &amp; CALLING</p>
      </header>
      <p class="author">T<span class="small-cap">OM</span> P<span class="small-cap">ETTIGREW</span></p>
    </section>

    <aside class="cover-spine">
      <div class="spine-text">
        <span class="spine-title">
          <span>WALKING BESIDE THE</span>
          <span class="spine-feature">QUIET</span>
          <span>RIVER</span>
        </span>
        <span class="spine-author">TOM PETTIGREW</span>
      </div>
    </aside>
  </main>
</body>
</html>
```